Kitchen and custom cabinetry company looking for business card design

We make: * Custom Kitchens, contemporary and traditional kitchens, Vanities, Libraries, Custom Entry Doors, Custom Wine Cellars and Custom Design Furniture. Phone number 555-318-2746. Address: Westhampton NY. Email: BRAVOK@mailbox.example Portfolio at: BRAVOKcabinetry.example I would like moderns fonts and not heavy lines. double side but maybe will use clear plastic. I attached the logo.

```html
<!DOCTYPE html>
<html lang="en">
<head>
<meta charset="utf-8">
<title>BRAVOK Cabinetry Inc. – Business Card</title>
<link href="https://fonts.googleapis.com/css2?family=Montserrat:ital,wght@0,500;1,700&family=Source+Sans+3:wght@400&display=swap" rel="stylesheet">
<style>
  :root {
    --orange: #f05a28;
    --grey: #7a7c7e;
    --ink: #1c1c1c;
    --white: #ffffff;
    --backdrop: #e9eaeb;
    --card: #fbfbfb;
  }
  * { margin: 0; padding: 0; box-sizing: border-box; }
  html, body { width: 1200px; height: 1000px; overflow: hidden; }
  body { background: var(--backdrop); font-family: "Source Sans 3", Arial, sans-serif; }

  .card {
    position: absolute;
    left: 237px; top: 278px;
    width: 851px; height: 498px;
    background: var(--card);
    box-shadow: 0 6px 24px rgba(0,0,0,0.10);
  }

  .brand {
    position: absolute;
    left: 33px; top: 34px;
    width: 390px;
  }
  .brand-name {
    font-family: "Montserrat", Arial, sans-serif;
    font-weight: 500;
    color: var(--grey);
    line-height: 1;
  }
  .brand-name .word { display: block; font-size: 90px; letter-spacing: 0; }
  .brand-name .suffix { display: block; font-size: 29px; letter-spacing: 10px; margin-top: 10px; white-space: nowrap; }
  .tagline {
    margin-top: 4px;
    font-family: "Source Sans 3", Arial, sans-serif;
    color: var(--orange);
    font-size: 17px;
    letter-spacing: 2.3px;
    white-space: nowrap;
  }

  .services {
    position: absolute;
    left: 0; top: 262px;
    width: 418px; height: 236px;
    background: var(--orange);
    border-top-right-radius: 22px;
    padding: 14px 0 0 34px;
    list-style: none;
  }
  .services li {
    color: var(--white);
    font-size: 22px;
    line-height: 27.5px;
    white-space: nowrap;
  }
  .services li::before { content: "• "; }

  .contact {
    position: absolute;
    right: 33px; top: 315px;
    list-style: none;
    text-align: right;
  }
  .contact li {
    display: flex;
    justify-content: flex-end;
    align-items: center;
    gap: 12px;
    height: 40.5px;
    font-size: 23px;
    color: var(--ink);
  }
  .contact .phone {
    font-family: "Montserrat", Arial, sans-serif;
    font-style: italic;
    font-weight: 700;
    font-size: 30px;
    letter-spacing: -0.5px;
  }
  .icon { width: 26px; height: 26px; flex: none; }
</style>
</head>
<body>
  <section class="card">
    <div class="brand">
      <div class="brand-name">
        <span class="word">BRAVOK</span>
        <span class="suffix">CABINETRY INC.</span>
      </div>
      <div class="tagline">CRAFTSMEN OF FINE INTERIOR WOODWORK</div>
    </div>

    <ul class="services">
      <li>Custom Kitchens</li>
      <li>Contemporary &amp; Traditional Kitchens</li>
      <li>Vanities</li>
      <li>Libraries</li>
      <li>Custom Entry Doors</li>
      <li>Custom Wine Cellars</li>
      <li>Custom Design Furniture</li>
    </ul>

    <ul class="contact">
      <li class="phone">555-318-2746
        <svg class="icon" viewBox="0 0 26 26" aria-hidden="true"><circle cx="13" cy="13" r="13" fill="#f05a28"/><path d="M9.5 7.5l2 3-1.3 1.3c.8 1.7 2 2.9 3.7 3.7l1.3-1.3 3 2-1.2 2c-4.5-.3-8.5-4.3-8.8-8.8z" fill="#fff"/></svg>
      </li>
      <li>BRAVOK@mailbox.example
        <svg class="icon" viewBox="0 0 26 26" aria-hidden="true"><circle cx="13" cy="13" r="13" fill="#f05a28"/><rect x="7" y="8.5" width="12" height="9" rx="1" fill="none" stroke="#fff" stroke-width="1.6"/><path d="M7.5 9.5l5.5 4.5 5.5-4.5" fill="none" stroke="#fff" stroke-width="1.6"/></svg>
      </li>
      <li>Lakeport, ME
        <svg class="icon" viewBox="0 0 26 26" aria-hidden="true"><circle cx="13" cy="13" r="13" fill="#f05a28"/><path d="M13 6.5a4.5 4.5 0 0 0-4.5 4.5c0 3.3 4.5 8.5 4.5 8.5s4.5-5.2 4.5-8.5A4.5 4.5 0 0 0 13 6.5z" fill="#fff"/><circle cx="13" cy="11" r="1.7" fill="#f05a28"/></svg>
      </li>
      <li>www.BRAVOKcabinetry.example
        <svg class="icon" viewBox="0 0 26 26" aria-hidden="true"><circle cx="13" cy="13" r="13" fill="#f05a28"/><g fill="none" stroke="#fff" stroke-width="1.8" stroke-linecap="round"><path d="M12 10.5l1.8-1.8a2.6 2.6 0 0 1 3.6 3.6L15.6 14"/><path d="M14 15.5l-1.8 1.8a2.6 2.6 0 0 1-3.6-3.6L10.4 12"/><path d="M11 15l4-4"/></g></svg>
      </li>
    </ul>
  </section>
</body>
</html>
```